Cookie Box Packaging

We are looking for a Box for our Shortbread Cookies. They are traditional shortbread middle to high end of the market. Made with butter. We already have a successful product and would like to use the brand but not necessarily the style.

We like our design to be an mix of vintage and modern - we are open to all colours. The competition on the supermarket shelf is stiff and we need to stand out in grocery not in the gourmet food market. Our thinking is simple rather than the craziness and chaos that comes with a supermarket shelf.
Attached are some Box Ideas, created in-house, along with a black shortbread box idea , which we loved but didn't really fit into the grocery section of the supermarket. Make us stand out in the grocery shelf! I have also uploaded a logo. Our brand is not necessary but, is there if you wanted to use it. I have also uploaded our other product/packet design so you can see the brand of our other cookie which is positioned in bakery /deli not grocery.

I look forward to seeing the results

```html
<!DOCTYPE html>
<html lang="en">
<head>
<meta charset="utf-8">
<title>Butter Shortbread – Box Front</title>
<link rel="stylesheet" href="https://fonts.googleapis.com/css2?family=Jost:wght@400;500;600&family=Lobster&display=swap">
<style>
  :root {
    --stripe-light: #f094be;
    --stripe-dark: #cd70a2;
    --title-pink: #ef8cbc;
    --ink: #1b1420;
    --white: #ffffff;
    --badge-blue: #2f6696;
    --biscuit: #e3a66a;
    --biscuit-deep: #c98a4d;
  }
  * { margin: 0; padding: 0; box-sizing: border-box; }
  html, body {
    width: 1200px; height: 1200px; overflow: hidden;
    background: var(--white);
    font-family: "Jost", sans-serif;
  }
  .canvas { position: relative; width: 1200px; height: 1200px; }
  .box-front {
    position: absolute; left: 50px; top: 326px;
    width: 1137px; height: 566px;
    transform: scale(0.9675); transform-origin: 0 0;
    overflow: hidden;
    background: repeating-linear-gradient(90deg,
      var(--stripe-light) 0 38px, var(--stripe-dark) 38px 76px);
  }
  .brand-name {
    position: absolute; left: 52px; top: 190px; width: 360px;
    font-family: "Jost", sans-serif; font-weight: 600;
    font-size: 62px; line-height: 1.02; color: var(--white);
    text-align: center;
  }
  .title-panel { position: absolute; left: 0; top: 0; width: 1137px; height: 340px; }
  .title-sub {
    position: absolute; left: 560px; top: 30px; width: 240px;
    font-family: "Lobster", cursive; font-size: 58px; line-height: 1;
    color: var(--white); text-align: center;
  }
  .title-main {
    position: absolute; left: 446px; top: 92px; width: 630px;
    font-family: "Lobster", cursive; font-size: 120px; line-height: 1;
    color: var(--title-pink); text-align: center;
    text-shadow: -4px 4px 0 var(--ink);
  }
  .product-photo {
    position: absolute; left: 588px; top: 232px; width: 400px; height: 292px;
    border-radius: 46% 40% 30% 36%;
    background: radial-gradient(ellipse at 45% 55%, var(--biscuit) 0 55%, var(--biscuit-deep) 80%, rgba(201,138,77,0) 100%);
  }
  .origin-badge {
    position: absolute; left: 414px; top: 414px; width: 112px; height: 112px;
    border-radius: 50%; background: var(--badge-blue);
  }
  .feature-list {
    position: absolute; left: 44px; top: 420px; list-style: none;
    font-size: 17px; line-height: 21.5px; color: var(--ink);
  }
  .feature-list li { display: flex; align-items: center; gap: 14px; }
  .feature-list svg { width: 14px; height: 14px; flex: none; }
  .net-weight {
    position: absolute; left: 1020px; top: 478px; width: 88px; height: 56px;
    border-radius: 50%; background: var(--white);
    display: flex; align-items: center; justify-content: center;
    font-weight: 600; font-size: 23px; color: var(--stripe-dark);
  }
</style>
</head>
<body>
<main class="canvas">
  <section class="box-front">
    <div class="brand-name">Bixby Biscuits</div>

    <svg class="title-panel" viewBox="0 0 1137 340" aria-hidden="true">
      <defs>
        <linearGradient id="panelFade" x1="0" y1="0" x2="0" y2="1">
          <stop offset="0" stop-color="#ffffff" stop-opacity="0.95"/>
          <stop offset="1" stop-color="#ffffff" stop-opacity="0.55"/>
        </linearGradient>
      </defs>
      <path fill="url(#panelFade)" d="M450 72 H570 Q580 72 584 82 L590 96 H812 L820 80 Q825 72 835 72 H1110 Q1126 74 1119 90 L1046 290 Q1036 312 1010 300 Q870 232 700 216 H450 Q440 216 440 206 V82 Q440 72 450 72 Z"/>
    </svg>
    <div class="title-sub">Butter</div>
    <div class="title-main">Shortbread</div>

    <div class="product-photo" role="img" aria-label="Photograph of stacked butter shortbread biscuits with a curl of butter"></div>

    <div class="origin-badge" role="img" aria-label="Country of origin badge"></div>

    <ul class="feature-list">
      <li><svg viewBox="0 0 14 14"><circle cx="7" cy="7" r="7" fill="var(--ink)"/><path d="M3.5 7.2 L6 9.5 L10.5 4.5" fill="none" stroke="var(--white)" stroke-width="1.8"/></svg>Lorem ipsum dolor sit amet, consec-</li>
      <li><svg viewBox="0 0 14 14"><circle cx="7" cy="7" r="7" fill="var(--ink)"/><path d="M3.5 7.2 L6 9.5 L10.5 4.5" fill="none" stroke="var(--white)" stroke-width="1.8"/></svg>tetuer adipiscing elit, sed diam</li>
      <li><svg viewBox="0 0 14 14"><circle cx="7" cy="7" r="7" fill="var(--ink)"/><path d="M3.5 7.2 L6 9.5 L10.5 4.5" fill="none" stroke="var(--white)" stroke-width="1.8"/></svg>nonummy nibh euismod tinc dolore</li>
      <li><svg viewBox="0 0 14 14"><circle cx="7" cy="7" r="7" fill="var(--ink)"/><path d="M3.5 7.2 L6 9.5 L10.5 4.5" fill="none" stroke="var(--white)" stroke-width="1.8"/></svg>magna aliquam erat volutpat.</li>
    </ul>

    <div class="net-weight">250g</div>
  </section>
</main>
</body>
</html>
```